SILVER FERN PORTRAITS photography made affordable

Photography made simple and affordable i provide back drop photography baby photography and childrens cake smash photography we also offer a range of back drops at a guaranteed affordable price we are a pop up studio we are a family owned business and we pride oursleves on making proffesional photography affordable for the average house hold we offer a variety of packages ranging from minis too larger values we are here to bring your memories to images for you too have forever and cherish

Target Market(s)

Baby photography portrait shots cake smash

Industry/Entity Type

Photography

Contact Information for Business Card

phone number 0417256849 EMAIL silverfernportraits@plumbox.net

Font styles to use
Decorative

Requirements
Must have
• A professional look
Nice to have
• Simple but eye catching

```html
<!DOCTYPE html>
<html lang="en">
<head>
<meta charset="utf-8">
<title>Silver Fern Portraits – Business Card</title>
<link href="https://fonts.googleapis.com/css2?family=Mulish:wght@400;600;800&display=swap" rel="stylesheet">
<style>
  :root {
    --page: #ece4d3;
    --card: #221b19;
    --white: #ffffff;
    --accent: #e39b12;
    --photo-light: #c9c7c4;
    --photo-dark: #8f8d8b;
  }
  * { margin: 0; padding: 0; box-sizing: border-box; }
  html, body {
    width: 1200px; height: 1200px; overflow: hidden;
    background: var(--page);
    font-family: "Mulish", sans-serif;
    color: var(--white);
  }
  .card {
    position: absolute;
    left: 210px;
    width: 780px; height: 440px;
    background: var(--card);
    box-shadow: 0 10px 24px rgba(0,0,0,0.25);
  }
  .card--front { top: 120px; }
  .card--back { top: 640px; }

  /* front */
  .photo-frame {
    position: absolute; left: 60px; top: 80px;
    width: 272px; height: 264px;
    border: 5px solid var(--accent);
  }
  .photo {
    position: absolute; left: 48px; top: 108px;
    width: 320px; height: 216px;
    background: linear-gradient(160deg, var(--photo-light), var(--photo-dark));
  }
  .front-brand {
    position: absolute; left: 390px; top: 60px; width: 360px;
    text-align: center;
  }
  .brand-mark {
    width: 72px; height: 72px; border-radius: 50%;
    border: 6px solid var(--accent);
    margin: 0 auto 16px;
  }
  .brand-name {
    font-weight: 800; font-size: 25px; letter-spacing: 0.5px;
    line-height: 1.05;
  }
  .brand-sub {
    font-weight: 400; font-size: 32px; line-height: 1.1;
  }
  .contact {
    position: absolute; left: 420px; top: 300px;
    list-style: none; font-size: 19px;
  }
  .contact li { display: flex; align-items: center; gap: 14px; margin-bottom: 14px; }
  .contact svg { width: 32px; height: 28px; flex: none; }

  /* back */
  .card--back .back-brand {
    position: absolute; left: 0; right: 0; top: 64px; text-align: center;
  }
  .card--back .brand-mark { width: 88px; height: 88px; border-width: 7px; margin-bottom: 18px; }
  .card--back .brand-name { font-size: 38px; }
  .card--back .brand-sub { font-size: 40px; }
  .tagline {
    position: absolute; left: 0; right: 0; top: 296px;
    text-align: center; color: var(--accent); font-size: 24px; font-weight: 600;
  }
  .about {
    position: absolute; left: 72px; right: 72px; top: 354px;
    font-size: 16px; line-height: 1.35; text-align: left;
  }
</style>
</head>
<body>
  <section class="card card--front">
    <div class="photo-frame"></div>
    <div class="photo" role="img" aria-label="Studio photograph of a festive snowman decoration"></div>
    <div class="front-brand">
      <div class="brand-mark"></div>
      <div class="brand-name">SILVER FERN PORTRAITS</div>
      <div class="brand-sub">photographers</div>
    </div>
    <ul class="contact">
      <li>
        <svg viewBox="0 0 32 28" fill="none" stroke="#fff" stroke-width="2.2" stroke-linecap="round">
          <path d="M6 4 L11 4 L13 10 L10 12 C12 17 15 20 20 22 L22 19 L28 21 L28 26 C16 26 6 16 6 4 Z"/>
          <path d="M18 8 a6 6 0 0 1 6 6"/><path d="M18 3 a11 11 0 0 1 11 11"/>
        </svg>
        <span>0417256849</span>
      </li>
      <li>
        <svg viewBox="0 0 32 28" fill="none" stroke="#fff" stroke-width="2.2" stroke-linejoin="round">
          <rect x="2" y="4" width="28" height="20"/>
          <path d="M2 4 L16 16 L30 4 M2 24 L12 13 M30 24 L20 13"/>
        </svg>
        <span>silverfernportraits@plumbox.net</span>
      </li>
    </ul>
  </section>

  <section class="card card--back">
    <div class="back-brand">
      <div class="brand-mark"></div>
      <div class="brand-name">SILVER FERN PORTRAITS</div>
      <div class="brand-sub">photographers</div>
    </div>
    <p class="tagline">Baby photography portrait - Cake smash sessions</p>
    <p class="about">We offer a variety of packages ranging from minis too larger values we are here to bring your memories to images for you too have forever and cherish</p>
  </section>
</body>
</html>
```